GREEN WILLOW LICE REMOVAL labels

I need a label design for our MINT REPELLING SHAMPOO (LICE PREVENTION).
It also includes our MINT REPELLING CONDITIONER (LICE PREVENTION) and our MINT SPRAY (LICE PREVENTION) also includes LICE & NIT ELIMINATING MOUSSE (LICE TREATMENT) and a LICE ELIMINATOR 100% Dimethicone oil (LICE TREATMENT). The shampoo and conditioner are sulfate free, contains peppermint and other essential oils and is safe for the entire family. Label should be simple, modern and high end looking. Fun is good too if it looks nice!

Target Market(s)

Kids and Adults

Industry/Entity Type

Hair Care Product

Font styles to use
Sans Serif
Decorative

Requirements
Must have
• -Words that should be used: safe, non toxic, sulfate free, essential oils, pesticide free. - Naturally removes lice, super lice & nits are great words for the lice & nit eliminating mousse and treatment oil 100% Dimethicone oil
- On a side note there are no essential oils in the lice & nit eliminating mousse or treatment oil 100% Dimethicone oil
Nice to have
• Earth tone colors if possible
Kid safe, no fillers, colors or scents
100% effective (even against super lice)
8oz labels and 4oz labels
Should not have
• No pictures of lice

```html
<!DOCTYPE html>
<html lang="en">
<head>
<meta charset="utf-8">
<title>Green Willow Lice Removal – Label Range</title>
<link href="https://fonts.googleapis.com/css2?family=Montserrat:wght@300;400;500;700;800&display=swap" rel="stylesheet">
<style>
  :root {
    --ink: #231f20;
    --rust: #c4512b;
    --tan: #a08a68;
    --silver: #a5a5a5;
    --leaf: #1f7a24;
    --paper: #ffffff;
    --backdrop: #f2f2f2;
    --edge: #dcdcdc;
  }
  * { box-sizing: border-box; margin: 0; padding: 0; }
  html, body {
    width: 1043px; height: 1200px; overflow: hidden;
    background: var(--backdrop);
    font-family: "Montserrat", sans-serif;
    color: var(--ink);
  }
  .range {
    display: flex; gap: 30px; justify-content: center;
    padding-top: 220px;
  }
  .label {
    position: relative;
    width: 300px; height: 760px;
    background: var(--paper);
    border: 1px solid var(--edge);
    border-radius: 6px;
    overflow: hidden;
  }
  .brand-vertical {
    position: absolute;
    left: 20px; bottom: 40px;
    transform-origin: left bottom;
    transform: rotate(-90deg) translateY(100%);
    white-space: nowrap;
    font-weight: 800; font-size: 66px; line-height: 1;
    letter-spacing: -1px;
    color: var(--ink);
  }
  .panel {
    position: absolute; left: 102px; right: 12px; top: 34px; bottom: 28px;
    display: flex; flex-direction: column;
  }
  .seal {
    display: flex; flex-direction: column; align-items: center; gap: 8px;
    margin-bottom: 40px;
  }
  .seal svg { width: 92px; height: 92px; }
  .seal-name {
    font-size: 9px; font-weight: 500; letter-spacing: 2px; text-align: center;
    color: var(--ink);
  }
  .title { font-weight: 800; font-size: 27px; line-height: 1.02; letter-spacing: -0.5px; white-space: nowrap; }
  .title .light { font-weight: 300; font-size: 40px; letter-spacing: 0; }
  .title .accent-tan { color: var(--tan); }
  .title .accent-silver { color: var(--silver); font-size: 23px; letter-spacing: -1px; }
  .title .accent-rust { color: var(--rust); font-size: 40px; }
  .tag {
    margin-top: 10px;
    padding: 4px 6px;
    color: #fff; font-size: 12px; letter-spacing: 2.5px; font-weight: 400;
    white-space: nowrap;
  }
  .tag.tan { background: var(--tan); }
  .tag.silver { background: var(--silver); }
  .organic { margin-top: 12px; font-size: 11px; letter-spacing: 5px; }
  .subproduct { margin-top: 12px; color: var(--tan); font-weight: 700; font-size: 15px; line-height: 1.05; }
  .treatment { margin-top: 6px; font-size: 11px; letter-spacing: 3.5px; }
  .claims { margin-top: auto; color: var(--leaf); font-weight: 500; font-size: 11px; line-height: 1.35; }
  .benefits { margin-top: 40px; font-size: 11px; line-height: 1.3; }
  .origin { margin-top: 34px; font-size: 9px; letter-spacing: 2px; text-align: center; margin-left: -40px; }
  .volume { margin-top: 12px; font-weight: 700; font-size: 12px; text-align: center; margin-left: -40px; }
</style>
</head>
<body>
<main class="range">

  <article class="label">
    <div class="brand-vertical">GREEN WILLOW</div>
    <div class="panel">
      <div class="seal">
        <svg viewBox="0 0 100 100" aria-hidden="true"><circle cx="50" cy="50" r="46" fill="none" stroke="var(--ink)" stroke-width="2"/></svg>
        <div class="seal-name">GREEN WILLOW<br>LICE REMOVAL</div>
      </div>
      <h2 class="title">MINT<br>REPELLING<br><span class="accent-tan">SHAMPOO</span></h2>
      <div class="tag tan">LICE PREVENTION</div>
      <div class="organic">100% ORGANIC</div>
      <p class="claims">Safe, Non toxic, Sulfate free,<br>Essential oils, Pesticide free</p>
      <p class="benefits">Naturally removes lice,<br>super lice &amp; nits are great<br>words for the lice &amp; nit<br>Eliminating Mousse<br>and Treatment oil<br>100% Dimethicone oil</p>
      <p class="origin">MADE IN COUNTRY NAME</p>
      <p class="volume">250 ml (8 fl. oz.)</p>
    </div>
  </article>

  <article class="label">
    <div class="brand-vertical">GREEN WILLOW</div>
    <div class="panel">
      <div class="seal">
        <svg viewBox="0 0 100 100" aria-hidden="true"><circle cx="50" cy="50" r="46" fill="none" stroke="var(--ink)" stroke-width="2"/></svg>
        <div class="seal-name">GREEN WILLOW<br>LICE REMOVAL</div>
      </div>
      <h2 class="title">MINT<br>REPELLING<br><span class="accent-silver">CONDITIONER</span></h2>
      <div class="tag silver">LICE PREVENTION</div>
      <div class="organic">100% ORGANIC</div>
      <p class="claims">Safe, Non toxic, Sulfate free,<br>Essential oils, Pesticide free</p>
      <p class="benefits">Naturally removes lice,<br>super lice &amp; nits are great<br>words for the lice &amp; nit<br>Eliminating Mousse<br>and Treatment oil<br>100% Dimethicone oil</p>
      <p class="origin">MADE IN COUNTRY NAME</p>
      <p class="volume">250 ml (8 fl. oz.)</p>
    </div>
  </article>

  <article class="label">
    <div class="brand-vertical">GREEN WILLOW</div>
    <div class="panel">
      <div class="seal">
        <svg viewBox="0 0 100 100" aria-hidden="true"><circle cx="50" cy="50" r="46" fill="none" stroke="var(--ink)" stroke-width="2"/></svg>
        <div class="seal-name">GREEN WILLOW<br>LICE REMOVAL</div>
      </div>
      <h2 class="title"><span class="light">MINT</span><br><span class="accent-rust">SPRAY</span></h2>
      <div class="tag silver">LICE PREVENTION</div>
      <div class="subproduct">LICE &amp; NIT<br>ELIMINATING<br>MOUSSE</div>
      <div class="treatment">LICE TREATMENT</div>
      <p class="claims">Safe, Non toxic, Sulfate free,<br>Essential oils, Pesticide free</p>
      <p class="benefits">Naturally removes lice,<br>super lice &amp; nits are great<br>words for the lice &amp; nit<br>Eliminating Mousse<br>and Treatment oil<br>100% Dimethicone oil</p>
      <p class="origin">MADE IN COUNTRY NAME</p>
      <p class="volume">250 ml (8 fl. oz.)</p>
    </div>
  </article>

</main>
</body>
</html>
```